Business card for real estate agent / office

We're looking for a new business card. We want something that is pretty clean, modern and sleek. Something that also tells people that we are a new age company...cutting edge. Although real estate has been done a certain way the last 100 years, we have energy and vibrance. Company name is Silver Meadow Properties. info can be found here: http://www.smprealtyhub.example/

needs to include: Name, title, phone number, email. our license number also needs to be displayed somewhere.

Target Market(s)

25-55 homeowners or potential homeowners

Industry/Entity Type

Business

Contact Information for Business Card

we need business card designs for real estate agent / office

Font styles to use
Serif

Requirements
Must have
• needs to include: Name, title, phone number, email. our license number also needs to be displayed somewhere and company name.
Nice to have
• placement area for photo

```html
<!DOCTYPE html>
<html lang="en">
<head>
<meta charset="utf-8">
<title>Silver Meadow Properties – Business Card</title>
<link href="https://fonts.googleapis.com/css2?family=Lora:wght@400;700&display=swap" rel="stylesheet">
<style>
  :root {
    --navy: #073f66;
    --green: #5aa83d;
    --white: #ffffff;
    --ground: #eeece6;
    --shadow: rgba(0, 0, 0, 0.22);
  }
  * { box-sizing: border-box; margin: 0; padding: 0; }
  html, body {
    width: 1200px; height: 929px; overflow: hidden;
    background: var(--ground);
    font-family: "Lora", serif;
  }
  .canvas { position: relative; width: 1200px; height: 929px; }
  .card {
    position: absolute; width: 560px; height: 320px;
    box-shadow: 0 6px 14px var(--shadow);
    overflow: hidden;
  }
  .card--front { left: 60px; top: 110px; background: var(--navy); }
  .card--back { left: 580px; top: 490px; background: var(--white); }

  .brand {
    position: absolute; left: 0; right: 0;
    display: flex; align-items: center; justify-content: center; gap: 12px;
    font-weight: 700; font-size: 32px; line-height: 1;
  }
  .brand__mark { width: 20px; height: 20px; flex: none; }
  .card--front .brand { top: 144px; color: var(--white); }
  .card--front .brand__mark { background: var(--white); }
  .card--back .brand { top: 76px; color: var(--navy); }
  .card--back .brand__mark { background: var(--green); }

  .info-band {
    position: absolute; left: 0; right: 0; bottom: 0; height: 128px;
    background: var(--navy); border-top: 4px solid var(--green);
  }
  .info-band::before {
    content: ""; position: absolute; left: 0; right: 0; top: -8px; height: 4px; background: var(--white);
  }
  .agent {
    position: absolute; right: 298px; top: 26px; text-align: right; color: var(--white);
  }
  .agent__name { font-size: 18px; font-weight: 400; letter-spacing: 0.5px; }
  .agent__title { font-size: 14px; margin-top: 4px; }
  .agent__license { font-size: 11px; margin-top: 6px; letter-spacing: 0.4px; opacity: 0.85; }
  .divider {
    position: absolute; left: 278px; top: 24px; width: 1px; height: 76px; background: var(--white);
  }
  .contacts {
    position: absolute; left: 298px; top: 26px; list-style: none; color: var(--white); font-size: 13px;
  }
  .contacts li { display: flex; align-items: center; gap: 10px; height: 24px; white-space: nowrap; }
  .contacts svg { width: 12px; height: 12px; flex: none; fill: none; stroke: var(--white); stroke-width: 1.6; }
</style>
</head>
<body>
<main class="canvas">
  <section class="card card--front" aria-label="Card front">
    <div class="brand"><span class="brand__mark"></span>Silver Meadow Properties</div>
  </section>

  <section class="card card--back" aria-label="Card back">
    <div class="brand"><span class="brand__mark"></span>Silver Meadow Properties</div>
    <div class="info-band">
      <div class="agent">
        <p class="agent__name">DANIEL HARTLEY</p>
        <p class="agent__title">Broker, Realtor, MBA</p>
        <p class="agent__license">License # 02187456</p>
      </div>
      <span class="divider"></span>
      <ul class="contacts">
        <li><svg viewBox="0 0 12 12"><rect x="3" y="1" width="6" height="10" rx="1"/></svg>310 555 0148</li>
        <li><svg viewBox="0 0 12 12"><rect x="1" y="2.5" width="10" height="7"/><path d="M1 2.5l5 4 5-4"/></svg>dan@smprealtyhub.example</li>
        <li><svg viewBox="0 0 12 12"><circle cx="5" cy="5" r="3.3"/><path d="M7.5 7.5L11 11"/></svg>www.smprealtyhub.example</li>
      </ul>
    </div>
  </section>
</main>
</body>
</html>
```